New business card for my lawn and landscape business

Dorrin Yard and Building is a full-service lawn care, landscaping, and light construction company serving Paragould and the Northeast Arkansas region. The business is owned and operated by Marcus Toller, with a reputation for hands-on, detail-oriented service, dependable crews, and quality results for both residential and commercial clients. A well regarded business with great reviews.
Owner Marcus Toller
Dorrinyardandbuilding.example

Target Market(s)

Commercial, Middle, and upper class in north east Arkansas

Industry/Entity Type

Lawn maintenance and landscape

Contact Information for Business Card

Dorrin Yard And Building Professional lawn care, landscaping, and property improvement in Northeast Arkansas. • lawn maintenance •lawn treatments and weed control • exterior projects • Custom landscape design & installation • Sod, trees, rock & drainage solutions • Residential & commercial services Reliable. Detailed. Done right.

Requirements
Must have
• Business name, service area, list of some of our services, clean design that represents
Nice to have
• Unique. Different design element than just grass because its already in n the logo. Picture of a warm season (south) lawn or landscape. Pictures of the type of work we do

```html
<!DOCTYPE html>
<html lang="en">
<head>
<meta charset="utf-8">
<title>Dorrin Yard and Building – Business Card</title>
<link rel="stylesheet" href="https://fonts.googleapis.com/css2?family=Raleway:ital,wght@0,500;0,600;0,700;1,600&display=swap">
<style>
  :root {
    --page: #ffffff;
    --card: #141414;
    --green: #7ab648;
    --white: #ffffff;
    --grey: #9a9a9c;
  }
  * { margin: 0; padding: 0; box-sizing: border-box; }
  html, body {
    width: 1200px; height: 1200px; overflow: hidden;
    background: var(--page);
    font-family: "Raleway", sans-serif;
  }
  .card {
    position: absolute;
    left: 124px; width: 960px; height: 548px;
    background: var(--card);
    box-shadow: 0 8px 14px rgba(0,0,0,0.45);
    color: var(--white);
    overflow: hidden;
  }
  .card--front { top: 24px; }
  .card--back { top: 613px; }

  /* front */
  .brand {
    position: absolute; left: 70px; top: 190px;
    display: flex; align-items: center; gap: 22px;
  }
  .brand__ring {
    width: 96px; height: 96px; border-radius: 50%;
    border: 6px solid var(--grey);
    flex: none;
  }
  .brand__name {
    color: var(--green); font-weight: 700;
    font-size: 38px; line-height: 1.15; letter-spacing: 1px;
  }
  .tagline {
    position: absolute; left: 21px; top: 446px;
    color: var(--green); font-style: italic; font-weight: 600;
    font-size: 33px; letter-spacing: 3px; white-space: nowrap;
  }
  .divider {
    position: absolute; left: 566px; top: 35px;
    width: 5px; height: 477px; background: var(--green);
  }
  .service {
    position: absolute; left: 575px; width: 385px; top: 56px;
    text-align: center;
  }
  .service__title { color: var(--green); font-weight: 500; font-size: 34px; line-height: 40px; }
  .service__area { margin-top: 8px; font-weight: 500; font-size: 28.5px; line-height: 50px; white-space: nowrap; }
  .contact {
    position: absolute; left: 594px; display: flex; align-items: center;
    font-weight: 500; font-size: 27px; white-space: nowrap;
  }
  .contact svg { width: 48px; height: 48px; flex: none; }
  .contact span { margin-left: 24px; }
  .contact--phone { top: 257px; }
  .contact--email { top: 344px; }
  .contact--web { top: 430px; }

  /* back */
  .intro {
    position: absolute; left: 20px; right: 20px; top: 36px;
    color: var(--green); font-weight: 500; font-size: 28.5px; line-height: 50px;
    text-align: center; white-space: nowrap;
  }
  .rule {
    position: absolute; left: 59px; width: 842px; top: 144px;
    height: 5px; background: var(--green);
  }
  .services {
    position: absolute; left: 59px; top: 174px; list-style: none;
    font-weight: 500; font-size: 28.5px; white-space: nowrap;
  }
  .services li { height: 44px; line-height: 44px; }
  .services li:nth-child(n+4) { height: 50px; line-height: 50px; }
  .services li::before { content: "•"; font-size: 18px; margin-right: 10px; vertical-align: 4px; }
</style>
</head>
<body>
  <section class="card card--front">
    <div class="brand">
      <div class="brand__ring"></div>
      <div class="brand__name">Dorrin Yard<br>and Building</div>
    </div>
    <p class="tagline">Reliable. Detailed. Done right</p>
    <div class="divider"></div>

    <div class="service">
      <p class="service__title">service area</p>
      <p class="service__area">Paragould and the<br>Northeast Arkansas region</p>
    </div>

    <div class="contact contact--phone">
      <svg viewBox="0 0 48 48" aria-hidden="true">
        <rect x="9" y="1" width="30" height="46" rx="4" fill="var(--green)"/>
        <circle cx="24" cy="6" r="1.3" fill="var(--card)"/>
        <circle cx="24" cy="42" r="1.6" fill="var(--card)"/>
      </svg>
      <span>123 456 789</span>
    </div>
    <div class="contact contact--email">
      <svg viewBox="0 0 48 48" aria-hidden="true">
        <rect x="1" y="6" width="46" height="36" rx="3" fill="var(--green)"/>
        <polyline points="5,9 24,28 43,9" fill="none" stroke="var(--card)" stroke-width="3"/>
      </svg>
      <span>info@dorrin.example</span>
    </div>
    <div class="contact contact--web">
      <svg viewBox="0 0 48 48" aria-hidden="true">
        <circle cx="24" cy="24" r="22" fill="var(--green)"/>
        <ellipse cx="24" cy="24" rx="8" ry="21" fill="none" stroke="var(--card)" stroke-width="3"/>
        <line x1="2" y1="24" x2="46" y2="24" stroke="var(--card)" stroke-width="3"/>
      </svg>
      <span>www.dorrin.example</span>
    </div>
  </section>

  <section class="card card--back">
    <p class="intro">Dorrin Yard And Building Professional lawn care,<br>landscaping, and property improvement in Northeast Arkansas.</p>
    <div class="rule"></div>
    <ul class="services">
      <li>lawn maintenance</li>
      <li>lawn treatments and weed control</li>
      <li>exterior projects</li>
      <li>Custom landscape design &amp; installation</li>
      <li>Sod, trees, rock &amp; drainage solutions</li>
      <li>Residential &amp; commercial services</li>
    </ul>
  </section>
</body>
</html>
```